Single brochure for international companies in the financial sector

We need to update a brochure 4 pages presenting our company. We are a financial engineering company. The final design must provide financial security, service and trust. you will find the current brochure copy. Our color code is Orange (RGB 235/100/68), Black, White and Gray. photos show the visual of the site, but it is not mandatory to keep them.

Target Market(s)

wealth management professionals

Industry/Entity Type

Finance

Requirements
Must have
• Logo Velbrook Capital all text in the document color Orange Velbrook (RGB 235/100/68)
Nice to have
• Vista Font
Should not have
• images / pictures of people

```html
<!DOCTYPE html>
<html lang="en">
<head>
<meta charset="utf-8">
<title>Velbrook Capital – Brochure</title>
<link rel="stylesheet" href="https://fonts.googleapis.com/css2?family=Fira+Sans:ital,wght@0,300;0,400;0,500;0,600;1,400&family=Jost:wght@300;400&display=swap">
<style>
  :root {
    --orange: #eb6444;
    --orange-soft: #ef7a5d;
    --orange-deep: #d9472b;
    --black: #222222;
    --text: #4a4a4a;
    --gray: #f2f2f2;
    --line: #c9c9c9;
    --white: #ffffff;
  }
  * { box-sizing: border-box; margin: 0; padding: 0; }
  html, body { width: 920px; height: 1200px; overflow: hidden; background: var(--white); }
  body { position: relative; font-family: "Fira Sans", Arial, sans-serif; color: var(--text); }

  .page {
    position: absolute;
    width: 352px;
    height: 498px;
    border: 1px solid var(--line);
    background: var(--white);
    overflow: hidden;
  }
  .page--cover   { left: 72px;  top: 57px; }
  .page--company { left: 498px; top: 57px; }
  .page--services{ left: 72px;  top: 630px; }
  .page--back    { left: 498px; top: 630px; }

  /* Cover */
  .cover-visual {
    position: absolute; left: 0; top: 0; width: 100%; height: 410px;
    background: linear-gradient(160deg, var(--orange-deep) 0%, var(--orange) 45%, var(--orange-soft) 100%);
  }
  .brand {
    position: absolute; left: 0; width: 100%; text-align: center;
    font-family: "Jost", "Futura", sans-serif; font-weight: 300; color: var(--white);
  }
  .brand__name { font-size: 30px; letter-spacing: 21px; padding-left: 21px; line-height: 1; }
  .brand__sub  { font-size: 22px; letter-spacing: 9px; padding-left: 9px; line-height: 1; margin-top: 18px; }
  .page--cover .brand { top: 216px; }
  .cover-tagline {
    position: absolute; left: 0; top: 478px; width: 100%; text-align: center;
    font-family: "Jost", "Futura", sans-serif; font-weight: 400;
    font-size: 14px; letter-spacing: 3.6px; color: var(--orange);
  }
  .page--cover .cover-tagline { top: 446px; }

  /* Inner pages */
  .hero {
    position: absolute; left: 0; top: 0; width: 100%; height: 109px;
    background: linear-gradient(180deg, #9a9a9a 0%, #3c3c3c 55%, #1e1e1e 100%);
  }
  .page--services .hero { background: linear-gradient(180deg, #d8d8d8 0%, #8a8a8a 50%, #3a3a3a 100%); }
  .band {
    position: absolute; left: 0; top: 109px; width: 100%; height: 29px;
    background: var(--orange); color: var(--white);
    font-weight: 500; font-size: 16px; letter-spacing: 2.4px;
    display: flex; align-items: center; justify-content: center;
  }
  .section {
    position: absolute; left: 0; width: 100%;
    display: flex; flex-direction: column; align-items: center; justify-content: center;
    text-align: center; padding: 0 20px;
  }
  .section--gray { background: var(--gray); }
  .pill {
    display: inline-block; background: var(--orange); color: var(--white);
    font-size: 12px; font-weight: 500; letter-spacing: 0.8px;
    padding: 2px 9px 3px; border-radius: 10px; margin-bottom: 8px;
  }
  .body-text { font-size: 9.2px; line-height: 15.5px; letter-spacing: 0.5px; color: var(--text); }
  .accent { color: var(--orange); }

  .quote {
    position: absolute; left: 0; top: 419px; width: 100%; height: 79px;
    background: var(--orange); color: var(--white);
    display: flex; align-items: center; justify-content: center; text-align: center;
  }
  .quote__text {
    font-size: 9px; font-weight: 600; letter-spacing: 0.8px; line-height: 14px;
    font-variant: small-caps; position: relative; padding: 0 26px;
  }
  .quote__mark { position: absolute; font-family: Georgia, serif; font-size: 22px; font-weight: 700; line-height: 1; }
  .quote__mark--open { left: 2px; top: -4px; }
  .quote__mark--close { right: 0; bottom: -12px; }

  .foot-strip { position: absolute; left: 0; top: 489px; width: 100%; height: 9px; background: var(--orange); }

  /* Back cover */
  .back-visual {
    position: absolute; left: 0; top: 0; width: 100%; height: 377px;
    background: linear-gradient(180deg, #f08a70 0%, var(--orange-soft) 40%, var(--orange) 100%);
  }
  .legal {
    position: absolute; left: 0; top: 298px; width: 100%; text-align: center;
    color: var(--white); font-size: 8.6px; line-height: 15.5px; letter-spacing: 0.4px;
  }
  .legal b { font-weight: 600; }
  .page--back .brand { top: 433px; color: var(--black); }
  .page--back .brand__name { font-size: 16px; letter-spacing: 11px; padding-left: 11px; }
  .page--back .brand__sub { font-size: 12px; letter-spacing: 4px; padding-left: 4px; margin-top: 8px; }
</style>
</head>
<body>

<section class="page page--cover">
  <div class="cover-visual" role="img" aria-label="Orange-tinted photo of a financial market chart on a screen"></div>
  <div class="brand">
    <div class="brand__name">VELBROOK</div>
    <div class="brand__sub">CAPITAL</div>
  </div>
  <p class="cover-tagline">FINANCIAL ENGINEERING</p>
</section>

<section class="page page--company">
  <div class="hero" role="img" aria-label="Black and white photo of a stone arch bridge"></div>
  <h2 class="band">THE COMPANY</h2>
  <div class="section section--gray" style="top:138px;height:88px;">
    <span class="pill">about us</span>
    <p class="body-text">Velbrook Capital is a <span class="accent">financial engineering company</span>.<br>It is fully independent from any bank or any other company.</p>
  </div>
  <div class="section" style="top:226px;height:103px;">
    <span class="pill">our clients</span>
    <p class="body-text">Our clients are financial professionals such as asset managers,<br>institutionnals, corporates, private banks, wealth managers and<br>family offices. Our purpose is to make their work easier, every day.</p>
  </div>
  <div class="section section--gray" style="top:329px;height:90px;">
    <span class="pill">what we do</span>
    <p class="body-text">We provide them with investment solutions de-signed to improve<br>their portfolios performance. <span class="accent">Simple as that.</span></p>
  </div>
  <div class="quote">
    <p class="quote__text">
      <span class="quote__mark quote__mark--open">&ldquo;</span>
      Our clients must deliver performance<br>on their portfolios on a regular basis.<br>We help them deliver everyday.
      <span class="quote__mark quote__mark--close">&rdquo;</span>
    </p>
  </div>
</section>

<section class="page page--services">
  <div class="hero" role="img" aria-label="Black and white photo of an old stone bridge under a cloudy sky"></div>
  <h2 class="band">OUR SERVICES</h2>
  <div class="section section--gray" style="top:138px;height:136px;">
    <span class="pill">investment advice</span>
    <p class="body-text"><span class="accent">Each client is looking for a unique investment solution.</span><br>Hence, we combine internal and external resources to create<br>the financial product that will best fit our clients requirements.<br>Thanks to a truly independent advice, we offer bespoke,<br>simple and efficient solutions.</p>
  </div>
  <div class="section" style="top:274px;height:114px;">
    <span class="pill">portfolio analysis</span>
    <p class="body-text">We advise our clients on their portfolios of financial products.<br>Together we identify the needs for restructuring or reallocating<br>the assets. We also provide full monitoring and reporting<br>services throughout the life of the products.</p>
  </div>
  <div class="section section--gray" style="top:388px;height:101px;">
    <span class="pill">partner selection</span>
    <p class="body-text">Our internal tools allow us to continuously assess the issuers<br>we are working with. Therefore we give our clients the luxury<br>to chose among the best issuers for their investment solution.</p>
  </div>
  <div class="foot-strip"></div>
</section>

<section class="page page--back">
  <div class="back-visual" role="img" aria-label="Orange-tinted photo of a stone arch bridge over a river"></div>
  <p class="legal">
    <b>Velbrook Capital SA. Capital :</b> 400 000 Euros<br>
    <b>RCS Paris :</b> 812 455 190<br>
    <b>Code Banque (CIB) :</b> 14207<br>
    www.velbrookcapital.com
  </p>
  <div class="brand">
    <div class="brand__name">VELBROOK</div>
    <div class="brand__sub">CAPITAL</div>
  </div>
</section>

</body>
</html>
```